Logistics Website Design

See website https://kravenfreightglobal.com for theme and color details. Need the site to be re-done and reflect some of the designs shown in this list here: https://pixelvane.com/tags/logistics-company-website

Target Market(s)

Logistics & Transportation

Industry/Entity Type

Logistics and Supply Chain

Coding

Coded - Design and coding required

Number of Pages Required

5+ page

Requirements
Must have
• Colors must match theme of logo. Looking for a sleek, interactive design.

```html
<!DOCTYPE html>
<html lang="en">
<head>
<meta charset="utf-8">
<title>Kraven Freight — Logistics & Transportation</title>
<link href="https://fonts.googleapis.com/css2?family=Bebas+Neue&family=Inter:wght@400;500;600&display=swap" rel="stylesheet">
<style>
:root{
  --bg:#150805;
  --bg-deep:#0f0604;
  --band:#2a0f08;
  --card:#24100a;
  --card-line:#5a2d1e;
  --orange:#e8673a;
  --orange-soft:#f28b5e;
  --text:#ffffff;
  --muted:#d7c3ba;
  --dim:#a8928a;
}
*{margin:0;padding:0;box-sizing:border-box}
html,body{width:1200px;height:4264px;overflow:hidden;background:var(--bg);color:var(--text);font-family:"Inter",sans-serif}
.page{position:relative;width:1200px;height:4264px;overflow:hidden}
.abs{position:absolute}
.display{font-family:"Bebas Neue",sans-serif;font-weight:400;letter-spacing:.5px;line-height:1}
.accent{color:var(--orange-soft)}
.btn{position:absolute;display:flex;align-items:center;justify-content:space-between;border-radius:30px;font-family:"Bebas Neue",sans-serif;font-size:17px;letter-spacing:.6px;color:#fff;padding:0 6px 0 24px;white-space:nowrap}
.btn-orange{background:var(--orange)}
.btn-dark{background:#1a0b07}
.btn-ghost{border:1.5px solid #8a6a5e;padding-left:6px}
.btn .arrow{flex:none;width:32px;height:32px;border-radius:50%;background:#1a0b07;display:flex;align-items:center;justify-content:center}
.btn-dark .arrow{background:var(--orange)}
.photo{position:absolute;overflow:hidden}

/* hero */
.hero{position:absolute;left:0;top:0;width:1200px;height:653px;background:linear-gradient(100deg,#2c140c 0%,#3a1b10 40%,#5b3a2c 70%,#6c4c40 100%)}
.logo{position:absolute;display:flex;align-items:center;gap:10px}
.logo .mark{width:40px;height:40px;border-radius:50%;background:var(--orange)}
.logo .name{font-family:"Bebas Neue",sans-serif;font-size:26px;color:#fff;letter-spacing:1px;white-space:nowrap}
.nav{position:absolute;top:34px;left:311px;font-family:"Inter",sans-serif;font-weight:600;font-size:13px}
.nav a{color:#fff;text-decoration:none;position:absolute;white-space:nowrap}

/* services */
.svc{position:absolute;top:1486px;width:256px;height:344px;background:var(--card);border:1px solid #4a2518;border-radius:6px;overflow:hidden;text-align:center}
.svc h3{font-family:"Bebas Neue",sans-serif;font-weight:400;font-size:25px;line-height:1.05;color:var(--orange-soft);margin-top:32px}
.svc p{font-size:11px;line-height:1.6;color:var(--muted);padding:0 26px;margin-top:14px}
.svc .photo{left:0;bottom:0;width:100%;height:120px}
.svc.active{background:var(--orange);border-radius:128px 128px 0 0;border:none}
.svc.active h3{color:#fff;margin-top:38px}
.svc.active p{color:#fde3d6}

/* industries */
.ind{position:absolute;width:339px;height:164px;border:1px solid var(--card-line);border-radius:4px;background:#170906;display:flex;gap:16px;padding:28px 20px 28px 24px}
.ind.hover{background:#2a130c}
.ind .icon{flex:none;width:58px;height:58px;border-radius:6px;background:var(--orange);display:flex;align-items:center;justify-content:center}
.ind h4{font-family:"Bebas Neue",sans-serif;font-weight:400;font-size:22px;color:var(--orange-soft);margin:6px 0 10px;white-space:nowrap}
.ind p{font-size:10.5px;line-height:1.6;color:var(--muted)}

/* testimonials */
.review{position:absolute;top:2720px;width:324px;height:265px;background:#2a120b;border-radius:4px;padding:36px 30px 36px 38px}
.review.mid{background:linear-gradient(180deg,#6b2d17,#3a160c)}
.review p{font-size:12px;line-height:1.9;color:var(--muted)}
.review .who{font-weight:600;font-size:15px;margin-top:12px}
.review .stars{color:var(--orange-soft);font-size:13px;letter-spacing:2px}
.review .src{position:absolute;right:30px;bottom:26px;width:18px;height:18px;border-radius:50%;border:3px solid var(--orange-soft)}

/* footer */
.fnav{position:absolute;left:365px;width:235px}
.fnav div{height:52px;border-bottom:1px solid #3a2018;display:flex;align-items:center;gap:22px;padding-left:20px;font-family:"Bebas Neue",sans-serif;font-size:25px}
.fnav div:last-child{border-bottom:none}
.field{position:absolute;left:883px;width:237px;height:36px;border:1px solid #8a6a5e;border-radius:2px;font-size:11px;color:var(--muted);display:flex;align-items:center;gap:8px;padding-left:14px}
</style>
</head>
<body>
<div class="page">

  <!-- HERO -->
  <section class="hero">
    <div class="photo" role="img" aria-label="White semi-truck with trailer driving on a highway at sunset" style="left:620px;top:105px;width:580px;height:548px;background:radial-gradient(ellipse at 55% 45%,#d9d6d4 0%,#9a8f8b 35%,#5d463d 65%,rgba(60,30,20,0) 85%)"></div>
    <div class="logo" style="left:82px;top:32px"><span class="mark"></span><span class="name">Kraven Freight</span></div>
    <nav class="nav">
      <a style="left:0">HOME</a>
      <a style="left:95px">SERVICES</a>
      <a style="left:212px">INDUSTRIES</a>
      <a style="left:330px">ABOUT US</a>
      <a style="left:436px">CONTACT US</a>
    </nav>
    <div class="btn btn-orange" style="left:945px;top:20px;width:178px;height:42px">REQUEST A QUOTE <span class="arrow"><svg width="14" height="14" viewBox="0 0 14 14"><path d="M3 11L11 3M5 3h6v6" stroke="#fff" stroke-width="1.6" fill="none"/></svg></span></div>

    <h1 class="display abs" style="left:114px;top:195px;font-size:68px"><span class="accent">Delivering Strength</span><br>In Every Mile</h1>
    <p class="abs" style="left:115px;top:348px;width:510px;font-size:16.5px;line-height:1.45;color:var(--muted)">We deliver a comprehensive range of open-deck and specialized transportation services—including flatbed, step deck, heavy haul, and over-dimensional freight solutions.</p>
    <div class="btn btn-orange" style="left:108px;top:448px;width:188px;height:44px">REQUEST A QUOTE <span class="arrow"><svg width="14" height="14" viewBox="0 0 14 14"><path d="M3 11L11 3M5 3h6v6" stroke="#fff" stroke-width="1.6" fill="none"/></svg></span></div>
    <div class="btn btn-ghost" style="left:305px;top:448px;width:165px;height:44px;justify-content:flex-start;gap:18px"><span class="arrow" style="background:var(--orange)"><svg width="14" height="14" viewBox="0 0 24 24"><path d="M6.6 10.8a15 15 0 006.6 6.6l2.2-2.2a1 1 0 011-.25 11 11 0 003.6.6 1 1 0 011 1V20a1 1 0 01-1 1A17 17 0 013 4a1 1 0 011-1h3.5a1 1 0 011 1 11 11 0 00.6 3.6 1 1 0 01-.25 1z" fill="#fff"/></svg></span>CALL US NOW</div>
  </section>
  <div class="abs" style="left:598px;top:612px;width:1px;height:68px;background:#9a7a6e"></div>

  <!-- ABOUT -->
  <section>
    <div class="photo" role="img" aria-label="Orange cab truck with trailer on a mountain highway" style="left:93px;top:800px;width:482px;height:372px;border-radius:10px;background:linear-gradient(180deg,#8fb3d6 0%,#b7c8d6 35%,#c77a3e 55%,#7a7a78 78%,#4a4844 100%)">
      <div class="abs" style="left:295px;top:308px;display:flex;align-items:center;gap:14px;font-family:'Bebas Neue',sans-serif;font-size:24px;color:#fff;white-space:nowrap">PLAY VIDEO <span style="width:44px;height:44px;border-radius:50%;background:#1a0b07;display:flex;align-items:center;justify-content:center"><svg width="14" height="16" viewBox="0 0 14 16"><path d="M1 1l12 7-12 7z" fill="#fff"/></svg></span></div>
    </div>
    <h2 class="display abs" style="left:631px;top:815px;font-size:56px"><span class="accent">Keeping Your Supply</span><br>Chain Moving</h2>
    <p class="abs" style="left:631px;top:945px;width:505px;font-size:16px;line-height:1.45;color:var(--muted)">We deliver a comprehensive range of open-deck and specialized transportation services—including flatbed, step deck, heavy haul, and over-dimensional freight solutions. Backed by years of experience, a trusted nationwide carrier network, and a strong safety-first culture, we provide reliable, adaptable logistics support built around the unique requirements of every load.</p>
    <div class="btn btn-orange" style="left:631px;top:1124px;width:162px;height:42px">LEARN MORE <span class="arrow"><svg width="14" height="14" viewBox="0 0 14 14"><path d="M3 11L11 3M5 3h6v6" stroke="#fff" stroke-width="1.6" fill="none"/></svg></span></div>
  </section>

  <!-- SERVICES -->
  <section class="abs" style="left:0;top:1316px;width:1200px;height:616px;background:var(--band)">
    <h2 class="display abs" style="left:0;top:70px;width:1200px;text-align:center;font-size:58px"><span class="accent">Our</span> Services</h2>
  </section>
  <article class="svc" style="left:70px">
    <h3>Flatbed<br>Transportation</h3>
    <p>From routine shipments to oversized and heavy-haul loads, we handle freight requiring proper securement, regulatory knowledge, and consistent on-time execution.</p>
    <div class="photo" role="img" aria-label="White box truck on a highway" style="background:linear-gradient(180deg,#2a120b,#8c8a88 60%,#5a5552)"></div>
  </article>
  <article class="svc active" style="left:345px">
    <h3>Step Deck<br>Transportation</h3>
    <p>Our step deck trucking services support tall, heavy, and specialized freight that requires additional height clearance and flexible loading options.</p>
    <div class="btn btn-dark" style="left:68px;top:205px;width:112px;height:30px;font-size:11px;padding-left:14px">LEARN MORE <span class="arrow" style="width:22px;height:22px"><svg width="10" height="10" viewBox="0 0 14 14"><path d="M3 11L11 3M5 3h6v6" stroke="#fff" stroke-width="1.8" fill="none"/></svg></span></div>
    <div class="photo" role="img" aria-label="Row of red step deck trailers" style="height:95px;background:linear-gradient(180deg,#e8673a,#b8342a 50%,#c9c2bf)"></div>
  </article>
  <article class="svc" style="left:611px">
    <h3>Step Deck<br>Transportation</h3>
    <p>From consumer goods to industrial materials, our dry van services provide the space, security, and consistency you need coast to coast.</p>
    <div class="photo" role="img" aria-label="Dry van truck on an open road between green fields" style="height:150px;background:linear-gradient(180deg,#2a120b,#5c6b3a 45%,#6a6a66)"></div>
  </article>
  <article class="svc" style="left:886px">
    <h3>Heavy Haul<br>Transportation</h3>
    <p>We provide heavy haul trucking solutions for oversized, overweight, and over-dimensional freight.</p>
    <div class="photo" role="img" aria-label="Red heavy haul truck carrying yellow equipment" style="height:140px;background:linear-gradient(180deg,#b9c2ca,#c8a23a 45%,#a8302a 70%,#55504c)"></div>
  </article>

  <!-- INDUSTRIES -->
  <h2 class="display abs" style="left:0;top:2015px;width:1200px;text-align:center;font-size:58px"><span class="accent">Industries</span> We Serve</h2>
  <div class="ind" style="left:83px;top:2127px"><span class="icon"><svg width="28" height="28" viewBox="0 0 24 24"><path d="M4 10h16l-2 10H6z M8 10l2-5 M16 10l-2-5" stroke="#fff" stroke-width="2" fill="none"/></svg></span><div><h4>Food &amp; Beverage</h4><p>Kraven Freight provides reliable, compliant, and efficient trucking solutions for the food and beverage industry.</p></div></div>
  <div class="ind hover" style="left:442px;top:2127px"><span class="icon"><svg width="28" height="28" viewBox="0 0 24 24"><path d="M3 4h3l2 11h11l2-8H7" stroke="#fff" stroke-width="2" fill="none"/><circle cx="10" cy="19" r="1.6" fill="#fff"/><circle cx="17" cy="19" r="1.6" fill="#fff"/></svg></span><div><h4>E-Commerce &amp; Retail</h4><p>Kraven Freight provides reliable, compliant, and efficient trucking solutions for the food and beverage industry.</p></div></div>
  <div class="ind" style="left:800px;top:2127px"><span class="icon"><svg width="28" height="28" viewBox="0 0 24 24"><circle cx="12" cy="8" r="3.5" stroke="#fff" stroke-width="2" fill="none"/><path d="M3 14h18v6H3z" stroke="#fff" stroke-width="2" fill="none"/></svg></span><div><h4>Manufacturing</h4><p>Kraven Freight provides reliable, compliant, and efficient trucking solutions for the food and beverage industry.</p></div></div>
  <div class="ind" style="left:243px;top:2313px"><span class="icon"><svg width="28" height="28" viewBox="0 0 24 24"><path d="M6 3h12v4H6z M5 7h14v14H5z M12 10v8 M8 14h8" stroke="#fff" stroke-width="2" fill="none"/></svg></span><div><h4>Pharma &amp; Healthcare</h4><p>Kraven Freight provides reliable, compliant, and efficient trucking solutions for the food and beverage industry.</p></div></div>
  <div class="ind" style="left:594px;top:2313px"><span class="icon"><svg width="28" height="28" viewBox="0 0 24 24"><path d="M12 3l9 5H3z M5 10v8 M9.7 10v8 M14.3 10v8 M19 10v8 M3 20h18" stroke="#fff" stroke-width="2" fill="none"/></svg></span><div><h4>Government</h4><p>Kraven Freight provides reliable, compliant, and efficient trucking solutions for the food and beverage industry.</p></div></div>

  <!-- TESTIMONIALS -->
  <h2 class="display abs" style="left:0;top:2618px;width:1200px;text-align:center;font-size:58px"><span class="accent">What</span> People Says</h2>
  <div class="review" style="left:109px"><p>"Lorem ipsum dolor sit amet, consectetur adipiscing elit, sed do eiusmod tempor incididunt ut labore et dolore magna aliqua. Quis ipsum suspendisse ultrices gravida. Risus commodo viverra maece-nas accumsan lacus vel facilisis"</p><div class="who">Mara Ellis</div><div class="stars">★★★★★</div><span class="src"></span></div>
  <div class="review mid" style="left:457px"><p>"Lorem ipsum dolor sit amet, consectetur adipiscing elit, sed do eiusmod tempor incididunt ut labore et dolore magna aliqua. Quis ipsum suspendisse ultrices gravida. Risus commodo viverra maece-nas accumsan lacus vel facilisis"</p><div class="who">Mara Ellis</div><div class="stars">★★★★★</div><span class="src"></span></div>
  <div class="review" style="left:805px"><p>"Lorem ipsum dolor sit amet, consectetur adipiscing elit, sed do eiusmod tempor incididunt ut labore et dolore magna aliqua. Quis ipsum suspendisse ultrices gravida. Risus commodo viverra maece-nas accumsan lacus vel facilisis"</p><div class="who">Mara Ellis</div><div class="stars">★★★★★</div><span class="src"></span></div>
  <svg class="abs" style="left:519px;top:3017px" width="176" height="32" aria-hidden="true">
    <circle cx="16" cy="16" r="15" fill="#5a2a1a"/><path d="M22 16H10m5-5l-5 5 5 5" stroke="#fff" stroke-width="2" fill="none"/>
    <circle cx="51" cy="16" r="3.5" fill="var(--orange)"/><circle cx="74" cy="16" r="3.5" fill="#fff"/><circle cx="97" cy="16" r="3.5" fill="#fff"/><circle cx="120" cy="16" r="3.5" fill="#fff"/>
    <circle cx="158" cy="16" r="15" fill="var(--orange)"/><path d="M152 16h12m-5-5l5 5-5 5" stroke="#fff" stroke-width="2" fill="none"/>
  </svg>

  <!-- CTA -->
  <section class="abs" style="left:37px;top:3143px;width:1126px;height:543px;border-radius:14px;overflow:hidden;background:linear-gradient(90deg,#d8643c 0%,#e46c3e 50%,#ee7b4c 100%)">
    <div class="photo" role="img" aria-label="White semi-truck cab with trailer on a road" style="left:0;top:30px;width:500px;height:513px;background:linear-gradient(100deg,#6a4c44 0%,#d8d4d2 45%,#a59a96 65%,rgba(216,100,60,0) 100%)"></div>
    <h2 class="display abs" style="left:595px;top:152px;font-size:58px">Request A Quote</h2>
    <p class="abs" style="left:595px;top:235px;width:500px;font-size:16px;line-height:1.5;color:#fde3d6">Lorem ipsum dolor sit amet, consectetur adipiscing elit, sed do eiusmod tempor incididunt ut labore et dolore magna aliqua. Quis ipsum suspendisse ultrices gravida.</p>
    <div class="btn btn-dark" style="left:595px;top:337px;width:173px;height:46px">GET IN TOUCH <span class="arrow"><svg width="14" height="14" viewBox="0 0 14 14"><path d="M3 11L11 3M5 3h6v6" stroke="#fff" stroke-width="1.6" fill="none"/></svg></span></div>
  </section>

  <!-- FOOTER -->
  <footer>
    <div class="logo" style="left:110px;top:3836px"><span class="mark" style="width:46px;height:46px"></span><span class="name" style="font-size:30px">Kraven Freight</span></div>
    <div class="abs" style="left:124px;top:3945px;display:flex;gap:14px">
      <span style="width:34px;height:34px;border-radius:50%;background:var(--orange)"></span>
      <span style="width:34px;height:34px;border-radius:50%;background:var(--orange)"></span>
      <span style="width:34px;height:34px;border-radius:50%;background:var(--orange)"></span>
    </div>
    <div class="abs" style="left:600px;top:3775px;width:1px;height:200px;background:#3a2018"></div>
    <div class="abs" style="left:845px;top:3775px;width:1px;height:200px;background:#3a2018"></div>
    <div class="fnav" style="top:3782px">
      <div><svg width="14" height="14" viewBox="0 0 24 24"><path d="M3 11l9-8 9 8v10H3z" fill="var(--orange)"/></svg>Home</div>
      <div><svg width="14" height="14" viewBox="0 0 24 24"><circle cx="12" cy="8" r="4" stroke="var(--orange)" stroke-width="2" fill="none"/><path d="M4 21c0-4 4-6 8-6s8 2 8 6" stroke="var(--orange)" stroke-width="2" fill="none"/></svg>About</div>
      <div><svg width="14" height="14" viewBox="0 0 24 24"><path d="M3 21V10l6 4V10l6 4V5h6v16z" fill="var(--orange)"/></svg>Industries</div>
      <div><svg width="14" height="14" viewBox="0 0 24 24"><path d="M6.6 10.8a15 15 0 006.6 6.6l2.2-2.2 4.6 1.6V21A17 17 0 013 4h4.8l1.6 4.6z" fill="var(--orange)"/></svg>Contact Us</div>
    </div>
    <div class="abs display" style="left:640px;top:3794px;font-size:24px;display:flex;gap:10px;align-items:center"><svg width="16" height="16" viewBox="0 0 24 24"><path d="M4 4l16 16M20 4L4 20" stroke="var(--orange)" stroke-width="3"/></svg>Services</div>
    <div class="abs display" style="left:670px;top:3836px;font-size:21px;line-height:36px;color:var(--orange-soft)">» Flatbed<br>» Step Deck<br>» Dry Van<br>» Heavy Haul</div>
    <div class="abs display" style="left:882px;top:3794px;font-size:24px">Contact Us</div>
    <div class="field" style="top:3833px"><svg width="11" height="11" viewBox="0 0 24 24"><circle cx="12" cy="8" r="5" fill="var(--orange)"/><path d="M3 22c0-5 4-8 9-8s9 3 9 8z" fill="var(--orange)"/></svg>Name</div>
    <div class="field" style="top:3880px"><svg width="11" height="11" viewBox="0 0 24 24"><path d="M2 5h20v14H2z" fill="var(--orange)"/></svg>Email address</div>
    <div class="field" style="top:3927px"><svg width="11" height="11" viewBox="0 0 24 24"><path d="M6.6 10.8a15 15 0 006.6 6.6l2.2-2.2 4.6 1.6V21A17 17 0 013 4h4.8l1.6 4.6z" fill="var(--orange)"/></svg>Phone</div>
    <div class="btn btn-orange" style="left:883px;top:3977px;width:112px;height:32px;font-size:12px;padding-left:18px">SEND NOW <span class="arrow" style="width:22px;height:22px"><svg width="10" height="10" viewBox="0 0 14 14"><path d="M3 11L11 3M5 3h6v6" stroke="#fff" stroke-width="1.8" fill="none"/></svg></span></div>

    <div class="abs" style="left:37px;top:4068px;width:1126px;height:1px;background:#3a2018"></div>
    <p class="abs" style="left:0;top:4097px;width:1200px;text-align:center;font-size:13px;color:var(--muted)">© 2026. An independent agent of Halvern Brook LLC.</p>
    <div class="abs" style="left:1063px;top:4086px;width:36px;height:36px;border-radius:50%;background:var(--orange);display:flex;align-items:center;justify-content:center"><svg width="16" height="16" viewBox="0 0 24 24"><path d="M12 3C6.5 3 3 6.6 3 11c0 2 .8 3.8 2.2 5.2L4 21l4.6-2c1 .3 2.2.5 3.4.5 5.5 0 9-3.6 9-8.5S17.5 3 12 3z" fill="#fff"/></svg></div>
    <div class="abs display" style="left:0;top:4162px;width:1200px;text-align:center;font-size:160px;color:#2a140d;letter-spacing:6px;white-space:nowrap">KRAVEN FREIGHT</div>
  </footer>

</div>
</body>
</html>
```